Restoration Specialist in need of business card designs

One side of the business card is a bathroom ripped out down to the studs with just a sink and toilet and then the other side is the bathroom (same sink and toilet) but put back together. Like a before and after on each side behind our information. Stand out, hard to forget, business cards for my restoration company. I want a unique concept all together.
Must include in no particular order:
our business name "Keystone Renewals"
Possible Logo for a restoration company
Owner; Martin Velasko
410-555-0192
mvelasko@keystonerenewalsMD.example
KeystoneRenewalsMD.example (our company website) BUT I am open to any and all designs and options.

Target Market(s)

Customers, Men in the mitigation, plumbing, electrical, HVAC, Roofing, insurance companies

Industry/Entity Type

Restoration/ construction

Contact Information for Business Card

Must include in no particular order: our business name "Keystone Renewals" Owner; Martin Velasko 410-555-0192 mvelasko@keystonerenewalsMD.example KeystoneRenewalsMD.example (our company website) MAY include a list of our services: Residential~ Emergency Response ~ Board- up~ Complete Restoration

Font styles to use
Serif

Colors
0054AA
0677BA
7BADD7
CADEEF
E8F1F8
F0912C
F2A743
F7CA91
FBE8D2
FDF5EE

Requirements
Must have
• unique, memorable, not something men have seen over and over again,
Nice to have
• eye catching
Should not have
• Been something I could have made by myself

```html
<!DOCTYPE html>
<html lang="en">
<head>
<meta charset="utf-8">
<title>Keystone Renewals – Business Card</title>
<link rel="stylesheet" href="https://fonts.googleapis.com/css2?family=Roboto+Slab:wght@700&family=Ubuntu:wght@400;500;700&display=swap">
<style>
  :root {
    --stage: #b3b3b3;
    --card: #161616;
    --house-grey: #a9a9a9;
    --orange: #f0812c;
    --white: #ffffff;
  }
  * { box-sizing: border-box; margin: 0; padding: 0; }
  html, body { width: 1200px; height: 866px; overflow: hidden; }
  body {
    background: var(--stage);
    display: flex;
    align-items: center;
    justify-content: center;
    gap: 40px;
    font-family: "Ubuntu", sans-serif;
  }
  .card {
    position: relative;
    width: 540px;
    height: 309px;
    background: var(--card);
    color: var(--white);
    overflow: hidden;
    box-shadow: 0 6px 18px rgba(0,0,0,.35);
  }
  .house-art {
    position: absolute;
    background: linear-gradient(160deg, var(--house-grey) 0%, #6f6f6f 55%, #3a3a3a 100%);
  }
  .front .house-art { left: 250px; top: 150px; width: 290px; height: 159px; }
  .back .house-art { left: 0; top: 195px; width: 250px; height: 114px; }

  /* front */
  .contact-block { position: absolute; left: 34px; top: 30px; z-index: 1; }
  .owner-name {
    font-family: "Roboto Slab", serif;
    font-weight: 700;
    color: var(--orange);
    font-size: 20px;
    letter-spacing: 1px;
    text-transform: uppercase;
  }
  .owner-role { font-size: 14px; font-weight: 500; margin: 2px 0 10px; }
  .contact-line {
    display: flex; align-items: center; gap: 8px;
    font-size: 13.5px; font-weight: 500; line-height: 20px;
  }
  .contact-line svg { width: 13px; height: 13px; flex: none; }
  .company-name {
    position: absolute;
    font-family: "Roboto Slab", serif;
    font-weight: 700;
    color: var(--orange);
    line-height: 1.02;
  }
  .front .company-name { left: 34px; top: 178px; font-size: 40px; }
  .back .company-name {
    right: 34px; bottom: 36px; font-size: 36px; text-align: right;
    display: flex; align-items: flex-start; gap: 10px;
  }
  .name-square { width: 14px; height: 14px; background: var(--orange); margin-top: 10px; flex: none; }

  /* back */
  .service-list { position: absolute; left: 44px; top: 36px; list-style: none; }
  .service-list li {
    display: flex; align-items: center; gap: 10px;
    font-weight: 700; font-size: 17px; line-height: 28px;
  }
  .bullet { width: 12px; height: 12px; flex: none; }
</style>
</head>
<body>
  <section class="card front" aria-label="Card front">
    <div class="house-art" role="img" aria-label="Grey house outline with chimney, smoke and window"></div>
    <div class="contact-block">
      <p class="owner-name">Martin Velasko</p>
      <p class="owner-role">Owner</p>
      <p class="contact-line">
        <svg viewBox="0 0 16 16" aria-hidden="true"><path fill="var(--orange)" d="M3.5 1l2.5 3-1.5 2c1 2 2.5 3.5 4.5 4.5l2-1.5 3 2.5-1.5 2.5C7.5 14.5 1.5 8.5 1 2.5z"/></svg>
        410-555-0192
      </p>
      <p class="contact-line">
        <svg viewBox="0 0 16 16" aria-hidden="true"><rect x="1" y="3" width="14" height="10" fill="var(--orange)"/><path d="M1 3l7 6 7-6" stroke="var(--card)" stroke-width="1.3" fill="none"/></svg>
        mvelasko@keystonerenewalsMD.example
      </p>
      <p class="contact-line">
        <svg viewBox="0 0 16 16" aria-hidden="true"><g fill="none" stroke="var(--orange)" stroke-width="1.5"><circle cx="8" cy="8" r="6.5"/><ellipse cx="8" cy="8" rx="3" ry="6.5"/><path d="M1.5 8h13M2.5 5h11M2.5 11h11"/></g></svg>
        KeystoneRenewalsMD.example
      </p>
    </div>
    <p class="company-name">Keystone<br>Renewals</p>
  </section>

  <section class="card back" aria-label="Card back">
    <div class="house-art" role="img" aria-label="Grey roof line of a house"></div>
    <ul class="service-list">
      <li><svg class="bullet" viewBox="0 0 12 12" aria-hidden="true"><rect width="5" height="5" fill="var(--orange)"/><rect x="7" width="5" height="5" fill="var(--white)"/><rect y="7" width="5" height="5" fill="var(--white)"/><rect x="7" y="7" width="5" height="5" fill="var(--orange)"/></svg>Residential</li>
      <li><svg class="bullet" viewBox="0 0 12 12" aria-hidden="true"><rect width="5" height="5" fill="var(--orange)"/><rect x="7" width="5" height="5" fill="var(--white)"/><rect y="7" width="5" height="5" fill="var(--white)"/><rect x="7" y="7" width="5" height="5" fill="var(--orange)"/></svg>Emergency Response</li>
      <li><svg class="bullet" viewBox="0 0 12 12" aria-hidden="true"><rect width="5" height="5" fill="var(--orange)"/><rect x="7" width="5" height="5" fill="var(--white)"/><rect y="7" width="5" height="5" fill="var(--white)"/><rect x="7" y="7" width="5" height="5" fill="var(--orange)"/></svg>Board- up</li>
      <li><svg class="bullet" viewBox="0 0 12 12" aria-hidden="true"><rect width="5" height="5" fill="var(--orange)"/><rect x="7" width="5" height="5" fill="var(--white)"/><rect y="7" width="5" height="5" fill="var(--white)"/><rect x="7" y="7" width="5" height="5" fill="var(--orange)"/></svg>Storm Protection</li>
      <li><svg class="bullet" viewBox="0 0 12 12" aria-hidden="true"><rect width="5" height="5" fill="var(--orange)"/><rect x="7" width="5" height="5" fill="var(--white)"/><rect y="7" width="5" height="5" fill="var(--white)"/><rect x="7" y="7" width="5" height="5" fill="var(--orange)"/></svg>Complete Restoration</li>
    </ul>
    <div class="company-name"><span class="name-square" aria-hidden="true"></span><p>Keystone<br>Renewals</p></div>
  </section>
</body>
</html>
```